Wine Labels for new product to attract Millenial consumers

SipRoam Design Brief
1. Intro:
Marrabel Cellars is a 120 year old family owned Australian wine company renowned for producing traditional premium quality wines. This project is aimed at breaking through this perception of Marrabel to show main stream Australian retailers that we can be innovative and relevant and that we know who their millennial shoppers are and we know how to attract their attention. This needs to be achieved through the combination of innovative and clever design paired with a product that challenges conventional Australian wine philosophies and appeals to those wine drinkers seeking authentic and alternative wine experiences.
2. Feelings:
This new wine should evoke a new set of feelings in retailers that they don’t usually associate with Marrabel Cellars. Retailers should feel excited, challenged and impressed by our knowledge of the millennial demographic. The packaging should make the shopper feel surprised, curious, cool, aspirational, understood, adventurous, individual, fashionable, progressive and engaged. It also needs to evoke a sense of the occasion it should be consumed in, with food and friends in a fun environment and evoke a sense of conviviality and a desire for shared social interaction.
3. Look + Feel:
It shouldn’t look or feel like anything Marrabel Cellars is known for and has done before. It should not carry our branding or logo, this should be a standalone product range. It should feel modern, cool, clever and hip. It should feel real, authentic, artisanal and most of all it should challenge the traditional visual discourse of wine as bored, tired, stiff and conservative. The design should be respected piece of art in its own right. It should make the shopper feel like getting a few friends around for dinner and drinks.
4. Brand Position:
This product range needs to challenge the existing brand positioning of Marrabel Cellars. It should clearly target the millennial demographic and the hipster sub culture who are being lured into new alcohol categories by cool design and positioning. “Exposed to a barrage of drinks offerings, the report found that wine is in danger of losing Generation Y to other more engaging drinks categories such as beer, cider and spirits ……. With 18-25 year olds accounting for 25% of the wine drinking population, Millennials represent an important sector of the wine market, thus keeping their attention and interest should remain a priority for wine brands.” Grape Insight Review. “…. Wine is becoming increasingly cool with the influencers and trend setters of a whole new generation.” Pour Journal.
5. Needs:
2 wine labels, one white and one red, but linked by design. Should fit a 500 ml glass bottle and design should be able to carry over to some innovative packaging into small lots of 4 or 6 like beer. For the purpose of design use the name SipRoam White and SipRoam Red. Relating the wine to food and how it should be consumed is important as this needs to be seen as a lifestyle accessory to food to combat the anti-alcohol lobby and the socially acceptable practise of eating and drinking together as part of a social experience. An area for approximately 200 words of mandatory information and declarations needs to be provided.

https://www.examplepins.test/MarrabelCellars/siproam-moodboard/

Full brief in project description

Requirements
Must have
• Full brief in project description
Nice to have
Should not have

```html
<!DOCTYPE html>
<html lang="en">
<head>
<meta charset="utf-8">
<title>SipRoam White and Red Labels</title>
<link href="https://fonts.googleapis.com/css2?family=Jost:wght@400&display=swap" rel="stylesheet">
<style>
  :root {
    --page: #ffffff;
    --label: #231f20;
    --chalk: #ffffff;
    --olive: #86752f;
    --vermilion: #f04e2c;
    --producer-grey: #c9c9c9;
  }
  html, body {
    margin: 0;
    padding: 0;
    width: 1108px;
    height: 1200px;
    overflow: hidden;
    background: var(--page);
    font-family: "Jost", "Futura", sans-serif;
  }
  .canvas {
    position: relative;
    width: 1108px;
    height: 1200px;
  }
  .label {
    position: absolute;
    width: 385px;
    height: 778px;
    background: var(--label);
    box-shadow: 2px 3px 6px rgba(0, 0, 0, 0.18);
  }
  .label--white { left: 115px; top: 113px; }
  .label--red { left: 607px; top: 304px; }

  .tile {
    position: absolute;
    width: 87px;
    height: 88px;
  }
  .tile--chalk { background: var(--chalk); }
  .tile--olive { background: var(--olive); }
  .tile--vermilion { background: var(--vermilion); }

  .col-1 { left: 33px; }
  .col-2 { left: 148px; }
  .col-3 { left: 265px; }
  .row-1 { top: 36px; }
  .row-2 { top: 162px; }
  .row-3 { top: 282px; }
  .row-4 { top: 408px; }
  .row-5 { top: 534px; }
  .row-foot { top: 657px; }

  .range-name {
    position: absolute;
    left: 358px;
    top: 158px;
    margin: 0;
    font-weight: 400;
    font-size: 124px;
    line-height: 88px;
    letter-spacing: 0;
    color: var(--chalk);
    white-space: nowrap;
    transform: rotate(90deg);
    transform-origin: 0 0;
  }

  /* statutory declarations block: producer statement and alcohol content */
  .mandatory-info {
    position: absolute;
    left: 0;
    top: 0;
    width: 0;
    height: 0;
  }
  .producer-statement {
    position: absolute;
    left: 38px;
    top: 651px;
    margin: 0;
    font-size: 20px;
    letter-spacing: 0.5px;
    color: var(--producer-grey);
    white-space: nowrap;
  }
  .alcohol-content {
    position: absolute;
    left: 43px;
    top: 729px;
    margin: 0;
    font-size: 17px;
    letter-spacing: 1px;
    color: var(--chalk);
    white-space: nowrap;
  }

  .variety {
    position: absolute;
    left: 218px;
    top: 746px;
    margin: 0;
    font-size: 21px;
    line-height: 22px;
    color: var(--chalk);
    white-space: nowrap;
    transform: rotate(-90deg);
    transform-origin: 0 0;
  }
  .variety--white { letter-spacing: 3px; }
  .variety--red { letter-spacing: 14px; font-size: 22px; }
</style>
</head>
<body>
<main class="canvas">

  <section class="label label--white" aria-label="SipRoam White label">
    <div class="tile tile--chalk col-1 row-1"></div>
    <div class="tile tile--olive col-2 row-1"></div>
    <div class="tile tile--vermilion col-3 row-1"></div>
    <div class="tile tile--chalk col-1 row-2"></div>
    <div class="tile tile--olive col-2 row-2"></div>
    <div class="tile tile--chalk col-1 row-3"></div>
    <div class="tile tile--olive col-2 row-3"></div>
    <div class="tile tile--chalk col-1 row-4"></div>
    <div class="tile tile--chalk col-1 row-5"></div>
    <h1 class="range-name">SipRoam</h1>
    <aside class="mandatory-info" aria-label="Mandatory information">
      <p class="producer-statement">Marrabel Cellars</p>
      <p class="alcohol-content">ALCOHOL 3.2%</p>
    </aside>
    <p class="variety variety--white">WHITE</p>
    <div class="tile tile--chalk col-3 row-foot"></div>
  </section>

  <section class="label label--red" aria-label="SipRoam Red label">
    <div class="tile tile--chalk col-1 row-1"></div>
    <div class="tile tile--olive col-2 row-1"></div>
    <div class="tile tile--vermilion col-3 row-1"></div>
    <div class="tile tile--chalk col-1 row-2"></div>
    <div class="tile tile--olive col-2 row-2"></div>
    <div class="tile tile--chalk col-1 row-3"></div>
    <div class="tile tile--olive col-2 row-3"></div>
    <div class="tile tile--chalk col-1 row-4"></div>
    <div class="tile tile--chalk col-1 row-5"></div>
    <h2 class="range-name">SipRoam</h2>
    <aside class="mandatory-info" aria-label="Mandatory information">
      <p class="producer-statement">Marrabel Cellars</p>
      <p class="alcohol-content">ALCOHOL 3.2%</p>
    </aside>
    <p class="variety variety--red">RED</p>
    <div class="tile tile--vermilion col-3 row-foot"></div>
  </section>

</main>
</body>
</html>
```